Design a Flyer for a master's thesis prize (ICT related topics)

An International Institute of Technology is going to offer a master’s thesis prize. The master’s thesis topic should be in the broad field of ICT. Prize includes money grant and a marvellous internship in premium hi-tech startup companies. It is required to design one big flyer accordingly in order to print it on A3/A2 paper size format. Good luck!

```html
<!DOCTYPE html>
<html lang="en">
<head>
<meta charset="utf-8">
<title>Master's Thesis Competition Flyer</title>
<link rel="stylesheet" href="https://fonts.googleapis.com/css2?family=PT+Sans+Narrow:wght@400;700&family=Source+Sans+3:wght@400;600;700&display=swap">
<style>
  :root {
    --backdrop: #aab5bf;
    --paper: #ffffff;
    --ink-title: #2a1520;
    --ink-dark: #231a22;
    --ink-navy: #1f3550;
    --prize-grey: #d4d4d6;
    --info-blue-top: #24578a;
    --info-blue-bottom: #173f66;
    --footer: #0f2b45;
    --photo-deep: #0c2236;
    --photo-mid: #2b6a93;
    --photo-cyan: #8fd0ea;
    --photo-violet: #c9a6dd;
  }
  * { margin: 0; padding: 0; box-sizing: border-box; }
  html, body {
    width: 919px; height: 1200px; overflow: hidden;
    background: var(--backdrop);
    font-family: "Source Sans 3", Arial, sans-serif;
  }
  .flyer {
    position: absolute; left: 93px; top: 84px;
    width: 714px; height: 1008px;
    background: var(--paper);
  }
  .institute {
    height: 76px;
    display: flex; align-items: center; justify-content: center;
    font-weight: 700; font-size: 29px;
    color: var(--ink-dark);
  }
  .hero { display: block; width: 714px; height: 529px; }
  .title-block { position: relative; height: 199px; text-align: center; }
  .title {
    position: absolute; left: 0; right: 0; top: 2px;
    font-family: "PT Sans Narrow", "Arial Narrow", sans-serif;
    font-weight: 700; font-size: 86px; line-height: 68px;
    color: var(--ink-title); white-space: nowrap;
    padding-top: 8px;
  }
  .field {
    position: absolute; left: 0; right: 0; top: 152px;
    font-family: "PT Sans Narrow", "Arial Narrow", sans-serif;
    font-size: 21px; letter-spacing: 3.6px;
    color: var(--ink-navy); white-space: nowrap;
  }
  .panels { display: flex; height: 172px; }
  .prize { width: 399px; background: var(--prize-grey); position: relative; }
  .trophy { position: absolute; left: 24px; top: 2px; width: 150px; height: 166px; }
  .prize-text {
    position: absolute; left: 165px; width: 210px; text-align: center;
    top: 42px;
    font-size: 32px; line-height: 36px; color: var(--ink-navy);
  }
  .info {
    flex: 1; position: relative; color: #fff;
    background: linear-gradient(180deg, var(--info-blue-top), var(--info-blue-bottom));
  }
  .info-heading {
    position: absolute; left: 75px; top: 20px;
    font-weight: 700; font-size: 26px; letter-spacing: 0.3px;
  }
  .info-details {
    position: absolute; left: 51px; top: 58px;
    font-size: 14px; line-height: 19px; color: #e6eef5;
  }
  .brand {
    position: absolute; left: 78px; top: 112px;
    font-weight: 700; font-size: 31px; letter-spacing: 1.5px; color: #e9eef3;
  }
  .footer {
    height: 33px; background: var(--footer);
    display: flex; align-items: center; justify-content: center;
    font-size: 10.5px; color: #d5dde5;
  }
</style>
</head>
<body>
  <main class="flyer">
    <header class="institute">INTERNATIONAL INSTITUTE OF TECHNOLOGY</header>

    <svg class="hero" viewBox="0 0 714 529" role="img" aria-label="Photo: a hand holding a floating laptop surrounded by glowing network icons, envelopes, a world map and a circuit board in deep blue tones">
      <defs>
        <linearGradient id="heroBase" x1="0" y1="0" x2="0.3" y2="1">
          <stop offset="0" stop-color="#3d7fa6"/>
          <stop offset="0.5" stop-color="var(--photo-mid)"/>
          <stop offset="1" stop-color="var(--photo-deep)"/>
        </linearGradient>
        <radialGradient id="heroCyan" cx="0.55" cy="0.4" r="0.45">
          <stop offset="0" stop-color="var(--photo-cyan)" stop-opacity="0.85"/>
          <stop offset="1" stop-color="var(--photo-cyan)" stop-opacity="0"/>
        </radialGradient>
        <radialGradient id="heroViolet" cx="0.36" cy="0.62" r="0.3">
          <stop offset="0" stop-color="#ffffff" stop-opacity="0.9"/>
          <stop offset="0.3" stop-color="var(--photo-violet)" stop-opacity="0.6"/>
          <stop offset="1" stop-color="var(--photo-violet)" stop-opacity="0"/>
        </radialGradient>
      </defs>
      <rect width="714" height="529" fill="url(#heroBase)"/>
      <rect width="714" height="529" fill="url(#heroCyan)"/>
      <rect width="714" height="529" fill="url(#heroViolet)"/>
    </svg>

    <section class="title-block">
      <h1 class="title">MASTER’S THESIS<br>COMPETITION</h1>
      <p class="field">INFORMATION AND COMMUNICATIONS TECHNOLOGY</p>
    </section>

    <section class="panels">
      <div class="prize">
        <svg class="trophy" viewBox="0 0 150 166" role="img" aria-label="Illustration: golden trophy cup on a black base with pink and gold fireworks behind">
          <defs>
            <radialGradient id="trophyTone" cx="0.5" cy="0.45" r="0.55">
              <stop offset="0" stop-color="#d8a23c"/>
              <stop offset="0.35" stop-color="#d6ae6a"/>
              <stop offset="0.7" stop-color="#e3c9c9"/>
              <stop offset="1" stop-color="#d4d4d6"/>
            </radialGradient>
          </defs>
          <rect width="150" height="166" fill="url(#trophyTone)"/>
        </svg>
        <p class="prize-text">WIN A MONEY<br>GRANT AND<br>INTERSHIP</p>
      </div>
      <div class="info">
        <h2 class="info-heading">INFORMATION:</h2>
        <p class="info-details">12:00, 25 March 2015<br>14B Via delle Arti<br>Rome, 00184, Italy</p>
        <p class="brand">NOVALINK</p>
      </div>
    </section>

    <footer class="footer">Copyright. All rights reserved 2015</footer>
  </main>
</body>
</html>
```